Real Estate "For Sale" Sign for construction company

We need a sign that we can use to hang on a post and place on the road when we sell a property. The sign will be simple and will need to mainly feature our logo (files attached), as well as the words "For Sale", and then our phone number "(555) 617 3489". The sign will hang on a post that'll look something like the attached picture.

Target Market(s)

Home buyers

Industry/Entity Type

Real Estate

Font styles to use
Serif
Sans Serif

Colors
0054AA
0677BA
7BADD7
CADEEF
E8F1F8
0094D4
00A9DD
6FCCEA
C7EBF8
E9F6FB

Requirements
Must have
• For Sale & our phone number

```html
<!DOCTYPE html>
<html lang="en">
<head>
<meta charset="UTF-8">
<title>For Sale Sign – Laurel Peak Homes</title>
<link href="https://fonts.googleapis.com/css2?family=Montserrat:wght@500;700&display=swap" rel="stylesheet">
<style>
  :root {
    --backdrop: #9b9b9b;
    --sign-bg: #b9e2f8;
    --headline: #378cba;
    --brand: #1f78b6;
    --pill: #378cba;
    --pill-text: #ffffff;
  }
  * { margin: 0; padding: 0; box-sizing: border-box; }
  html, body {
    width: 1200px;
    height: 2435px;
    overflow: hidden;
    background: var(--backdrop);
  }
  .canvas {
    position: relative;
    width: 1200px;
    height: 2435px;
  }
  .sign {
    position: absolute;
    left: 50px;
    top: 483px;
    width: 1100px;
    height: 1469px;
    background: var(--sign-bg);
    box-shadow: 14px 18px 40px rgba(0, 0, 0, 0.35);
    font-family: "Montserrat", Arial, sans-serif;
  }
  .brand {
    position: absolute;
    top: 250px;
    left: 0;
    width: 100%;
    display: flex;
    justify-content: center;
    align-items: center;
    gap: 24px;
  }
  .brand-mark {
    width: 56px;
    height: 56px;
    border-radius: 50%;
    background: var(--brand);
  }
  .brand-name {
    font-weight: 500;
    font-size: 70px;
    line-height: 1;
    color: var(--brand);
  }
  .headline {
    position: absolute;
    top: 528px;
    left: 0;
    width: 100%;
    text-align: center;
    font-weight: 700;
    font-size: 268px;
    line-height: 252px;
    letter-spacing: 4px;
    color: var(--headline);
  }
  .phone {
    position: absolute;
    left: 168px;
    top: 1185px;
    width: 766px;
    height: 112px;
    border-radius: 56px;
    background: var(--pill);
    color: var(--pill-text);
    display: flex;
    align-items: center;
    justify-content: center;
    gap: 18px;
    font-weight: 700;
    font-size: 80px;
    line-height: 1;
  }
  .phone-icon { width: 52px; height: 52px; }
</style>
</head>
<body>
<div class="canvas">
  <div class="sign">
    <div class="brand">
      <span class="brand-mark"></span>
      <span class="brand-name">Laurel Peak Homes</span>
    </div>
    <h1 class="headline">FOR<br>SALE</h1>
    <div class="phone">
      <svg class="phone-icon" viewBox="0 0 24 24" aria-hidden="true">
        <path fill="#ffffff" d="M6.6 10.8a15.1 15.1 0 0 0 6.6 6.6l2.2-2.2c.3-.3.7-.4 1-.2 1.1.4 2.3.6 3.6.6.6 0 1 .4 1 1V20c0 .6-.4 1-1 1A17 17 0 0 1 3 4c0-.6.4-1 1-1h3.5c.6 0 1 .4 1 1 0 1.3.2 2.5.6 3.6.1.3 0 .7-.2 1z"/>
        <path fill="none" stroke="#ffffff" stroke-width="1.6" stroke-linecap="round" d="M14.5 3.5a6 6 0 0 1 6 6M14.5 6.8a2.8 2.8 0 0 1 2.8 2.8"/>
      </svg>
      <span class="phone-number">(555) 617 3489</span>
    </div>
  </div>
</div>
</body>
</html>
```